Naturopath Practitioner Card Design

I am a naturopath needing a design for a business card mainly to show that I am a naturopath and have some contact details to give to prospective clients. I am open minded about the design and what is on the second side of the card whether it just be some artwork or space for details, appointment times etc. Naturopathy is the practice of natural medicine that uses a holistic approach and incorporates herbal and nutritional medicine.

Contact Information for Business Card

Tom Waverly NaturopathBHSc (Naturopathy) Member NHPG 0491 582 736 tom.waverly@mailbox-example.net www.tomwaverlynaturopathy.example.au

Requirements
Nice to have
• Would prefer some kind of original pattern/art work/logo rather than an image, not fussed if its very simple/basic
• I am open to any colour but think I would prefer a more earthy sandy clay etc type style than the greens that are commonly associated with naturopathy.
Should not have
• Don't really want to have generic stock images on it

```html
<!DOCTYPE html>
<html lang="en">
<head>
<meta charset="utf-8">
<title>Tom Waverly Naturopath – Business Card</title>
<link rel="stylesheet" href="https://fonts.googleapis.com/css2?family=Didact+Gothic&display=swap">
<style>
  :root {
    --backdrop: #e6e6e4;
    --paper: #ffffff;
    --clay: #5b4620;
    --clay-dark: #4a3918;
    --gold: #c9a840;
    --ochre: #8a6d1f;
    --ink: #4d4d4d;
  }
  * { margin: 0; padding: 0; box-sizing: border-box; }
  html, body { width: 1200px; height: 1021px; overflow: hidden; }
  body {
    background: var(--backdrop);
    font-family: "Didact Gothic", "Century Gothic", sans-serif;
    display: flex;
    align-items: center;
    justify-content: center;
    gap: 50px;
  }
  .card {
    position: relative;
    width: 525px;
    height: 300px;
    box-shadow: 0 6px 18px rgba(0,0,0,0.18);
  }

  /* Contact side */
  .card--contact { background: var(--paper); }
  .contact__header {
    position: absolute;
    top: 52px;
    left: 0;
    right: 0;
    text-align: center;
  }
  .contact__name {
    font-size: 27px;
    color: var(--ink);
    letter-spacing: 0.5px;
    font-weight: 400;
  }
  .contact__credentials {
    margin-top: 6px;
    font-size: 12.5px;
    color: var(--ochre);
  }
  .contact__rule {
    position: absolute;
    left: 175px;
    right: 30px;
    top: 150px;
    height: 5px;
    background: var(--clay);
  }
  .contact__details {
    position: absolute;
    left: 175px;
    right: 30px;
    top: 170px;
    display: flex;
    justify-content: space-between;
    font-size: 12.5px;
    color: var(--ink);
  }
  .contact__item { display: flex; align-items: center; gap: 6px; }
  .contact__item svg { width: 14px; height: 14px; fill: var(--clay); }
  .contact__brand {
    position: absolute;
    left: 32px;
    bottom: 34px;
    display: flex;
    align-items: center;
    gap: 8px;
    font-size: 14px;
    color: var(--clay);
  }
  .brand-dot {
    width: 16px; height: 16px; border-radius: 50%;
    background: var(--clay);
  }

  /* Brand side */
  .card--brand {
    background: var(--clay);
    background-image: radial-gradient(circle at 40% 35%, #63502a 0%, var(--clay) 55%, var(--clay-dark) 100%);
  }
  .brand__lockup {
    position: absolute;
    top: 62px;
    left: 0; right: 0;
    display: flex;
    flex-direction: column;
    align-items: center;
  }
  .brand__mark {
    width: 46px; height: 46px; border-radius: 50%;
    background: var(--gold);
    margin-bottom: 18px;
  }
  .brand__name {
    font-size: 40px;
    color: var(--gold);
    letter-spacing: 1px;
    line-height: 1;
  }
  .brand__role {
    margin-top: 6px;
    font-size: 13px;
    letter-spacing: 6px;
    color: var(--gold);
  }
  .brand__web {
    position: absolute;
    bottom: 42px;
    left: 0; right: 0;
    text-align: center;
    font-size: 15px;
    color: #f2efe6;
    letter-spacing: 0.4px;
  }
</style>
</head>
<body>
  <section class="card card--contact">
    <div class="contact__header">
      <h1 class="contact__name">Tom Waverly</h1>
      <p class="contact__credentials">BHSc (Naturopathy) Member NHPG</p>
    </div>
    <div class="contact__rule"></div>
    <div class="contact__details">
      <span class="contact__item">
        <svg viewBox="0 0 16 16" aria-hidden="true"><path d="M2 5c0-2 2-3 6-3s6 1 6 3v1h-3V5H5v1H2z M4 7h8l2 6H2z M6 9a2 2 0 1 0 4 0a2 2 0 1 0-4 0z"/></svg>
        0491 582 736
      </span>
      <span class="contact__item">
        <svg viewBox="0 0 16 16" aria-hidden="true"><path d="M1 4h14v9H1z" fill="none"/><path d="M1 3h14v1L8 9 1 4z M1 5l7 5 7-5v8H1z"/></svg>
        tom.waverly@mailbox-example.net
      </span>
    </div>
    <div class="contact__brand">
      <span class="brand-dot"></span>
      <span>Tom Waverly</span>
    </div>
  </section>

  <section class="card card--brand">
    <div class="brand__lockup">
      <span class="brand__mark"></span>
      <span class="brand__name">Tom Waverly</span>
      <span class="brand__role">Naturopath</span>
    </div>
    <p class="brand__web">www.tomwaverlynaturopathy.example.au</p>
  </section>
</body>
</html>
```